tamo rix

TAMO RIX mobile technology servicesPhone and tablet repairs, screens data recovery.

Industry/Entity Type

Data Recovery

Contact Information for Business Card

0431 587 612

Colors
33a6d7
f04a50
0a90cc
e34197

Requirements
Must have
• Gary plinth
Nice to have
• White background

```html
<!DOCTYPE html>
<html lang="en">
<head>
<meta charset="utf-8">
<title>Tamo Rix – Business Card</title>
<link rel="stylesheet" href="https://fonts.googleapis.com/css2?family=Open+Sans:wght@400;600;700;800&display=swap">
<style>
  :root {
    --backdrop: #e7e4df;
    --card-orange: #e8821c;
    --brand-orange: #e0661f;
    --accent-orange: #ea8a12;
    --paper: #f5f3ef;
    --ink-grey: #555555;
    --white: #ffffff;
  }
  * { margin: 0; padding: 0; box-sizing: border-box; }
  html, body {
    width: 1200px;
    height: 955px;
    overflow: hidden;
    background: var(--backdrop);
    font-family: "Open Sans", Arial, sans-serif;
  }
  .business-card {
    position: absolute;
    left: 100px;
    top: 192px;
    width: 1000px;
    height: 570px;
    background: var(--card-orange);
    box-shadow: 0 6px 18px rgba(0,0,0,0.18);
    overflow: hidden;
  }
  .brand-panel {
    position: absolute;
    left: 150px;
    top: 0;
    width: 360px;
    height: 100%;
    background: var(--paper);
  }
  .tagline {
    position: absolute;
    right: 34px;
    top: 34px;
    text-align: right;
    font-weight: 600;
    font-size: 21px;
    line-height: 1.1;
    color: var(--ink-grey);
  }
  .brand-name {
    position: absolute;
    right: 30px;
    top: 100px;
    text-align: right;
    font-weight: 800;
    font-size: 108px;
    line-height: 0.95;
    letter-spacing: -2px;
    color: var(--brand-orange);
  }
  .service-list {
    position: absolute;
    right: 34px;
    bottom: 40px;
    text-align: right;
    font-size: 23px;
    line-height: 1.15;
    color: var(--ink-grey);
  }
  .service-list .service-highlight {
    display: block;
    font-weight: 700;
    color: var(--accent-orange);
    margin-bottom: 14px;
  }
  .service-list .service-highlight:last-child { margin-bottom: 0; }
  .contact-panel {
    position: absolute;
    left: 510px;
    top: 0;
    width: 490px;
    height: 100%;
    color: var(--white);
  }
  .person-name {
    position: absolute;
    left: 50px;
    top: 62px;
    font-weight: 700;
    font-size: 60px;
    line-height: 1;
  }
  .contact-line {
    position: absolute;
    left: 56px;
    display: flex;
    align-items: center;
    gap: 22px;
    font-weight: 600;
    font-size: 30px;
  }
  .contact-line svg { flex: none; }
  .contact-phone { top: 200px; }
  .contact-email { top: 340px; }
  .contact-web { top: 418px; }
</style>
</head>
<body>
  <div class="business-card">
    <section class="brand-panel">
      <p class="tagline">mobile technology<br>services</p>
      <h1 class="brand-name">TAMO<br>RIX</h1>
      <p class="service-list">
        Phone and tablet
        <span class="service-highlight">REPAIRS</span>
        Data
        <span class="service-highlight">RECOVERY</span>
      </p>
    </section>
    <section class="contact-panel">
      <h2 class="person-name">Gary plinth</h2>
      <p class="contact-line contact-phone">
        <svg width="30" height="34" viewBox="0 0 24 24" aria-hidden="true">
          <path fill="#ffffff" d="M6.6 2.5c.6-.3 1.3-.1 1.6.5l1.8 3.4c.3.6.1 1.3-.4 1.6l-1.5 1c.8 2 2.3 3.8 4.2 5l1.2-1.3c.5-.5 1.2-.6 1.7-.2l3.2 2.1c.6.4.7 1.1.4 1.7l-1.1 1.9c-.6 1-1.8 1.5-2.9 1.2C8.6 17.8 4.2 12.3 3.2 6.7c-.2-1.1.3-2.2 1.3-2.8z"/>
        </svg>
        0431 587 612
      </p>
      <p class="contact-line contact-email">
        <svg width="40" height="28" viewBox="0 0 40 28" aria-hidden="true">
          <rect x="1" y="1" width="38" height="26" fill="#ffffff"/>
          <path d="M2 3 L20 16 L38 3" fill="none" stroke="#e8821c" stroke-width="3"/>
        </svg>
        repair@tamorix.me
      </p>
      <p class="contact-line contact-web">
        <svg width="40" height="40" viewBox="0 0 40 40" aria-hidden="true">
          <rect x="1" y="1" width="38" height="38" fill="#ffffff"/>
          <text x="20" y="30" text-anchor="middle" font-family="Open Sans, Arial, sans-serif" font-weight="700" font-size="28" fill="#e8821c">e</text>
        </svg>
        www.tamorix.me
      </p>
    </section>
  </div>
</body>
</html>
```